依頼詳細
現在使っているものを画像データで添付します。
事務所ロゴをフォトショップデータで添付します。

参考に、市販の表紙デザインにはこういったものがあります。(下記リンク)
https://www.kazane-dk.co.jp/store/products/list.php?category_id=23
https://tomoriworks.com/item/certificate/
http://mizuho-kanade.com/front_cover/
A4の紙を綴じるものなので、A3より一回り大きいA3ワイドのレザック紙に印刷しております。こちら302×430mmサイズです。

表紙には、お客様(権利者)の名前と
その下には不動産の表示が入ります。(案件ごとに印刷します)
そのため、こちらを手差し印刷できるよう、高さ5センチ程度の空白を空けておいていただきたいです。

サイズ:A3ワイド(302×430mm)
2つ折り、左開きです。半分に折った部分が表紙となります。

色、デザインの雰囲気等お任せいたします。
公的で固い重要書類をいれるものですが、そういったイメージにはあまり縛られずなるべくオリジナリティのあるものを使いたいと思います。
記載項目
不動産登記権利情報

司法書士ふじさわ事務所
希望イメージ
シンプル 複雑
単色 カラフル
暗い 明るい
日常 高級
遊び心 厳粛
未来的 伝統的
女性的 男性的
希望する色
設定なし
納品ファイル
• イラストレーター形式 (.ai)
補足説明
設定なし
【追記】桐のマークについて
現在使っている権利証表紙には、司法書士バッヂの意匠である五三桐花をいれておりますが、今回は特に使用の指定はしません。
桐のマークを入れる場合については、五三桐でお願いいたします(葉っぱが中央に5枚・左右に3枚ずつの家紋)

(参考)
http://senra-mokudo.com/kamon-c/cate0/kiri/kiri2.html
https://www.ezukan-store.jp/img344/225970_3130817.html
■ 選んだ理由

見た瞬間に目を惹くデザインだと思い、選ばせていただきました。

■ 提案者全員のお礼・コメント

たくさんのご提案をいただき大変嬉しく思っております。
皆様それぞれ、素敵なデザインを考えていただき本当にありがとうございます。

```html
<!DOCTYPE html>
<html lang="ja">
<head>
<meta charset="utf-8">
<title>不動産登記 権利情報 — 表紙</title>
<link href="https://fonts.googleapis.com/css2?family=Shippori+Mincho:wght@500;600&family=Cormorant+Garamond:wght@500&display=swap" rel="stylesheet">
<style>
  :root {
    --paper: #efebe3;
    --band: #e3ded3;
    --footer: #f5f2ec;
    --gold: #a8843c;
    --gold-light: #c9ad72;
    --ink: #262422;
    --rule: #cfc8b9;
    --card: #ffffff;
  }
  * { margin: 0; padding: 0; box-sizing: border-box; }
  html, body { width: 855px; height: 1200px; overflow: hidden; background: var(--paper); }
  .cover {
    position: relative; width: 855px; height: 1200px;
    background: var(--paper);
    font-family: "Shippori Mincho", serif; color: var(--ink);
  }
  .cover__border {
    position: absolute; inset: 14px; border: 1px solid var(--rule); pointer-events: none;
  }
  .header-band {
    position: absolute; top: 0; left: 0; right: 0; height: 112px;
    background: var(--band); border-bottom: 1px solid var(--rule);
  }
  .header-band__label {
    position: absolute; top: 44px;
    font-family: "Cormorant Garamond", serif; font-size: 13px; letter-spacing: 0.12em;
    color: #6e665a; white-space: nowrap;
  }
  .header-band__label--left { left: 48px; }
  .header-band__label--right { right: 48px; }
  .header-band__rule { position: absolute; top: 52px; height: 1px; background: var(--gold-light); }
  .header-band__rule--left { left: 345px; width: 45px; }
  .header-band__rule--right { left: 465px; width: 45px; }
  .header-band__dot {
    position: absolute; left: 400px; top: 20px; width: 56px; height: 56px;
    border-radius: 50%; background: var(--gold-light);
  }
  .title {
    position: absolute; left: 0; right: 0; text-align: center;
  }
  .title--main { top: 168px; font-size: 80px; font-weight: 500; letter-spacing: 0.16em; padding-left: 0.16em; }
  .title--sub { top: 290px; font-size: 56px; font-weight: 500; letter-spacing: 0.06em; padding-left: 0.06em; }
  .print-area {
    position: absolute; left: 114px; top: 436px; width: 627px; height: 328px;
  }
  .print-area svg { display: block; }
  .footer {
    position: absolute; left: 0; right: 0; bottom: 0; height: 236px;
    background: var(--footer); border-top: 1px solid var(--rule); text-align: center;
  }
  .footer__role { margin-top: 36px; font-size: 27px; font-weight: 500; letter-spacing: 0.05em; }
  .footer__name { margin-top: 6px; font-size: 54px; font-weight: 600; letter-spacing: 0.08em; }
</style>
</head>
<body>
<main class="cover">
  <header class="header-band">
    <span class="header-band__label header-band__label--left">FUJISAWA JUDICIAL SCRIVENER OFFICE</span>
    <span class="header-band__rule header-band__rule--left"></span>
    <span class="header-band__dot" aria-hidden="true"></span>
    <span class="header-band__rule header-band__rule--right"></span>
    <span class="header-band__label header-band__label--right">Real Estate Registration Right Information</span>
  </header>

  <h1 class="title title--main">不動産登記</h1>
  <h2 class="title title--sub">権利情報</h2>

  <section class="print-area" aria-label="権利者名・不動産の表示 記入欄">
    <svg width="627" height="328" viewBox="0 0 627 328">
      <rect x="20" y="14" width="587" height="300" fill="var(--card)" stroke="var(--rule)"/>
      <g fill="none" stroke="var(--gold)" stroke-width="5">
        <path d="M2 40 V2 H40"/>
        <path d="M587 2 H625 V40"/>
        <path d="M2 288 V326 H40"/>
        <path d="M587 326 H625 V288"/>
      </g>
      <g stroke="var(--gold-light)" stroke-width="2" stroke-dasharray="4 3">
        <line x1="57" y1="52" x2="570" y2="52"/>
        <line x1="57" y1="58" x2="570" y2="58"/>
        <line x1="57" y1="274" x2="570" y2="274"/>
        <line x1="57" y1="280" x2="570" y2="280"/>
      </g>
      <line x1="57" y1="166" x2="570" y2="166" stroke="var(--rule)" stroke-width="1.5"/>
    </svg>
  </section>

  <footer class="footer">
    <p class="footer__role">司法書士・行政書士</p>
    <p class="footer__name">ふじさわ事務所</p>
  </footer>

  <div class="cover__border"></div>
</main>
</body>
</html>
```